Regional Consulting Business Needs a Business Card Design

We need a business card design for our new business based in Regional Victoria, Australia called Velor Power. We are a consulting company with our main goal being to save people momey money and reducing their carbon footprint. Anything from water saving showerheads, to energy saving lightglobes and even to solar power. We would like to see designs that use bright colours. The final design should shout 'we are here to help you'.

Industry/Entity Type

Business

```html
<!DOCTYPE html>
<html lang="en">
<head>
<meta charset="utf-8">
<title>Velor Power – Business Card</title>
<link rel="stylesheet" href="https://fonts.googleapis.com/css2?family=Libre+Franklin:wght@800&family=Open+Sans:wght@400;600&display=swap">
<style>
  :root {
    --backdrop: #3c3c3c;
    --silver-light: #fbfbfb;
    --silver-mid: #e4e4e4;
    --silver-dark: #cfcfcf;
    --charcoal: #4a4a4a;
    --orange: #f2ad22;
    --orange-light: #f6bb3a;
    --white: #ffffff;
  }
  * { margin: 0; padding: 0; box-sizing: border-box; }
  html, body { width: 1200px; height: 900px; overflow: hidden; }
  body {
    position: relative;
    background: var(--backdrop);
    font-family: "Open Sans", Arial, sans-serif;
  }
  .card {
    position: absolute;
    top: 300px;
    width: 524px;
    height: 298px;
    border-radius: 18px;
    overflow: hidden;
    background: linear-gradient(160deg, var(--silver-mid) 0%, var(--silver-light) 38%, var(--silver-mid) 55%, var(--silver-dark) 100%);
  }
  .card--front { left: 58px; }
  .card--back { left: 618px; }

  .brand-name {
    font-family: "Libre Franklin", Arial, sans-serif;
    font-weight: 800;
    color: var(--charcoal);
    letter-spacing: -0.5px;
    white-space: nowrap;
  }
  .brand-mark {
    display: inline-block;
    background: var(--orange);
  }
  .tagline {
    font-weight: 600;
    color: var(--charcoal);
    white-space: nowrap;
  }

  /* Front */
  .front-lockup {
    position: absolute;
    left: 0; right: 0;
    top: 200px;
    text-align: center;
  }
  .front-lockup .brand-row {
    display: inline-flex;
    align-items: center;
    gap: 14px;
  }
  .front-lockup .brand-mark { width: 34px; height: 34px; }
  .front-lockup .brand-name { font-size: 44px; line-height: 50px; }
  .front-lockup .tagline { font-size: 12.5px; margin-top: 2px; }

  /* Back */
  .back-header {
    position: absolute;
    left: 0; top: 0;
    width: 100%;
    height: 150px;
  }
  .back-header .brand-row {
    position: absolute;
    left: 120px; top: 56px;
    display: flex;
    align-items: center;
    gap: 12px;
  }
  .back-header .brand-mark { width: 26px; height: 26px; }
  .back-header .brand-name { font-size: 32px; line-height: 38px; }
  .back-header .tagline {
    position: absolute;
    left: 187px; top: 93px;
    font-size: 9.5px;
  }
  .contact-band {
    position: absolute;
    left: 0; top: 150px;
    width: 100%;
    height: 148px;
    background: linear-gradient(180deg, var(--orange-light), var(--orange));
    color: var(--white);
  }
  .band-notch { position: absolute; left: 66px; top: 150px; }
  .person { position: absolute; left: 47px; top: 28px; }
  .person-name { font-size: 17px; font-weight: 600; }
  .person-role { font-size: 11.5px; margin-left: 6px; }
  .contact-lines { position: absolute; left: 47px; top: 60px; font-size: 12px; line-height: 15.5px; }
  .website { position: absolute; left: 47px; top: 100px; font-size: 14.5px; }
  .divider {
    position: absolute;
    left: 310px; top: 33px;
    width: 1px; height: 108px;
    background: rgba(255,255,255,0.7);
  }
  .address { position: absolute; left: 329px; top: 29px; font-size: 12px; line-height: 15.5px; }
  .phones { position: absolute; left: 329px; top: 91px; font-size: 12px; line-height: 15.5px; }
</style>
</head>
<body>

  <section class="card card--front">
    <div class="front-lockup">
      <div class="brand-row">
        <span class="brand-mark"></span>
        <span class="brand-name">Velor Power</span>
      </div>
      <p class="tagline">Maintanence and consulting services</p>
    </div>
  </section>

  <section class="card card--back">
    <header class="back-header">
      <div class="brand-row">
        <span class="brand-mark"></span>
        <span class="brand-name">Velor Power</span>
      </div>
      <p class="tagline">Maintanence and consulting services</p>
    </header>

    <div class="contact-band">
      <p class="person"><span class="person-name">John Doe</span><span class="person-role">Manager</span></p>
      <p class="contact-lines">Mobile: 000 000 000<br>Email: johndoe@velorpower.com</p>
      <p class="website">www.VelorPower.com</p>
      <span class="divider"></span>
      <p class="address">00 Your Street<br>000000 000 000 0000<br>PO Box 000</p>
      <p class="phones">Ph: +00 7 0000 0000<br>Fax: + 00 7 0000 0000</p>
    </div>

    <svg class="band-notch" width="36" height="18" viewBox="0 0 36 18" aria-hidden="true">
      <polygon points="1,0 35,0 18,17" fill="#ffffff"/>
      <polygon points="8,0 28,0 18,10" fill="#4a4a4a"/>
    </svg>
  </section>

</body>
</html>
```